Stationary & Business Cards
Brimford Holdings
Project: Stationary & Business Cards
Stationary & Business Cards - Construction
Creative Brief
Simple
Dale Purcott
General Manager
P.O. Box 382 Ashbury CT 06218
Dale@BrimfordHoldings.com
ON THE STATIONARY ONLY: add our website www.BrimfordHoldings.com
logo to fill in entire back of business card. (Red background with blue lettering)

```html
<!DOCTYPE html>
<html lang="en">
<head>
<meta charset="utf-8">
<title>Brimford Holdings – Business Cards</title>
<link rel="stylesheet" href="https://fonts.googleapis.com/css2?family=Oswald:wght@400;600&family=Roboto+Condensed:wght@400;700&display=swap">
<style>
  :root {
    --navy: #1f3a6e;
    --red: #c8282e;
    --ink: #333840;
    --muted: #6b7078;
    --card: #ffffff;
    --backdrop: #e4e5e7;
  }
  * { box-sizing: border-box; margin: 0; padding: 0; }
  html, body { width: 1200px; height: 946px; overflow: hidden; }
  body {
    background: var(--backdrop);
    font-family: "Roboto Condensed", Arial, sans-serif;
    color: var(--ink);
    position: relative;
  }
  .card {
    position: absolute;
    left: 250px;
    width: 700px;
    height: 400px;
    background: var(--card);
    border-radius: 22px;
    box-shadow: 0 6px 18px rgba(0,0,0,0.12);
    overflow: hidden;
  }
  .card--back { top: 48px; background: var(--red); }
  .card--front { top: 498px; }

  .brand {
    display: flex;
    align-items: center;
    gap: 10px;
  }
  .brand__name {
    font-family: "Oswald", Arial, sans-serif;
    font-weight: 600;
    color: var(--navy);
    text-transform: uppercase;
    line-height: 1;
    letter-spacing: 1px;
    white-space: nowrap;
  }
  .brand__mark {
    width: 14px; height: 14px;
    background: var(--red);
    flex: none;
  }
  .brand__tag {
    font-family: "Oswald", Arial, sans-serif;
    font-weight: 600;
    color: var(--navy);
    font-size: 9px;
    letter-spacing: 3px;
    text-transform: uppercase;
    margin-top: 6px;
  }

  /* back: red full-bleed with navy lettering */
  .card--back .brand-block {
    position: absolute;
    left: 0; right: 0; top: 0; bottom: 0;
    display: flex; flex-direction: column; align-items: center; justify-content: center;
  }
  .card--back .brand__name { font-size: 68px; letter-spacing: 2px; }
  .card--back .brand__tag { font-size: 15px; letter-spacing: 6px; margin-top: 14px; }
  .social {
    position: absolute;
    right: 34px; bottom: 26px;
    display: flex; gap: 18px;
  }
  .social__item { display: flex; align-items: center; gap: 6px; font-size: 12px; color: #fff; }
  .social__box { width: 14px; height: 14px; background: var(--navy); }

  /* front */
  .card--front .brand-block {
    position: absolute;
    left: 40px; top: 168px;
    display: flex; flex-direction: column; align-items: flex-start;
  }
  .card--front .brand__name { font-size: 30px; }
  .details {
    position: absolute;
    left: 372px; top: 70px;
    display: flex; flex-direction: column; gap: 34px;
  }
  .detail { display: flex; align-items: center; gap: 16px; }
  .detail__icon { width: 30px; height: 30px; flex: none; }
  .detail__rule { width: 3px; align-self: stretch; background: var(--ink); }
  .detail__text { font-size: 15px; line-height: 1.45; letter-spacing: 0.5px; }
  .person__name {
    font-family: "Oswald", Arial, sans-serif;
    font-size: 26px; font-weight: 400;
    text-transform: uppercase; letter-spacing: 2px; line-height: 1.1;
  }
  .person__role { font-size: 14px; color: var(--muted); }
</style>
</head>
<body>

<section class="card card--back" aria-label="Business card back">
  <div class="brand-block">
    <div class="brand">
      <span class="brand__name">Brimford Holdings</span>
    </div>
    <div class="brand__tag">Est. 1998</div>
  </div>
  <div class="social">
    <div class="social__item"><span class="social__box"></span>/brimford</div>
    <div class="social__item"><span class="social__box"></span>/brimford</div>
  </div>
</section>

<section class="card card--front" aria-label="Business card front">
  <div class="brand-block">
    <div class="brand">
      <span class="brand__name">Brimford Holdings</span>
      <span class="brand__mark"></span>
    </div>
    <div class="brand__tag">Est. 1998</div>
  </div>

  <div class="details">
    <div class="detail">
      <svg class="detail__icon" viewBox="0 0 30 30" aria-hidden="true">
        <circle cx="15" cy="9" r="6.5" fill="var(--navy)"/>
        <path d="M3 28c0-7 5.5-11 12-11s12 4 12 11z" fill="var(--navy)"/>
      </svg>
      <span class="detail__rule"></span>
      <div class="detail__text">
        <div class="person__name">Dale Purcott</div>
        <div class="person__role">General Manager</div>
      </div>
    </div>

    <div class="detail">
      <svg class="detail__icon" viewBox="0 0 30 30" aria-hidden="true">
        <path d="M15 2a9 9 0 0 0-9 9c0 7 9 17 9 17s9-10 9-17a9 9 0 0 0-9-9z" fill="var(--navy)"/>
        <circle cx="15" cy="11" r="3.5" fill="#fff"/>
      </svg>
      <span class="detail__rule"></span>
      <div class="detail__text">
        <div>P.O. Box 382</div>
        <div>Ashbury CT 06218</div>
      </div>
    </div>

    <div class="detail">
      <svg class="detail__icon" viewBox="0 0 30 30" aria-hidden="true" fill="none" stroke="var(--navy)" stroke-width="2">
        <circle cx="15" cy="15" r="12"/>
        <ellipse cx="15" cy="15" rx="5" ry="12"/>
        <line x1="3" y1="15" x2="27" y2="15"/>
        <line x1="5" y1="9" x2="25" y2="9"/>
        <line x1="5" y1="21" x2="25" y2="21"/>
      </svg>
      <span class="detail__rule"></span>
      <div class="detail__text">
        <div>012 555 0187</div>
        <div>Dale@BrimfordHoldings.com</div>
      </div>
    </div>
  </div>
</section>

</body>
</html>
```